Q5 Pops (CBD candy infused with Delta-8)

The proposed logo are two pool table balls. One is a D and the other is an 8, its a brand and we need a label for Gummy human treats. This treats are being infused with Delt-8. I i will upload examples only. The example is of the type of labels needed (package and label for bottle)

Target Market(s)

Your professionals

Font styles to use
Sans Serif

Requirements
Must have
• Youthful look
Nice to have
• Consider using the Delta symbol instead of the D.
Also, I provided a sample of a label that's used on two type of packages.

```html
<!DOCTYPE html>
<html lang="en">
<head>
<meta charset="utf-8">
<title>Q5 Pops – Delta-8 candy pouches</title>
<link rel="stylesheet" href="https://fonts.googleapis.com/css2?family=Barlow:wght@400;600;800&family=Barlow+Condensed:wght@500;700&family=Dancing+Script:wght@700&display=swap">
<style>
  :root {
    --stage: #dcdad8;
    --red: #e0141b;
    --red-deep: #a80c10;
    --black: #0b0b0b;
    --white: #ffffff;
    --silver: #e9e9ea;
    --silver-dark: #cfd0d2;
    --grey-text: #4b4b4b;
    --green: #1f8a3a;
    --green-deep: #0f5c24;
    --candy-a: #f2c84a;
    --candy-b: #ef7a4c;
    --candy-c: #8fcf6a;
    --wood: #c49a66;
  }
  * { margin: 0; padding: 0; box-sizing: border-box; }
  html, body { width: 1200px; height: 879px; overflow: hidden; }
  body { background: var(--stage); position: relative; font-family: "Barlow", sans-serif; }
  .pouch { position: absolute; width: 383px; height: 555px; display: block; }
  .pouch--silver { left: 160px; top: 188px; }
  .pouch--green { left: 630px; top: 184px; }
  .brand-name { font-family: "Barlow", sans-serif; font-weight: 800; }
  .tagline { font-family: "Barlow", sans-serif; font-weight: 400; }
  .product-name { font-family: "Barlow Condensed", sans-serif; font-weight: 700; letter-spacing: 1px; }
  .icon-caption { font-family: "Barlow Condensed", sans-serif; font-weight: 500; }
  .dose { font-family: "Barlow", sans-serif; font-weight: 600; }
  .dose-bold { font-family: "Barlow Condensed", sans-serif; font-weight: 700; }
  .script { font-family: "Dancing Script", cursive; font-weight: 700; }
  .ribbon-text { font-family: "Barlow", sans-serif; font-weight: 600; }
</style>
</head>
<body>

<!-- Silver pouch -->
<svg class="pouch pouch--silver" viewBox="0 0 383 555" aria-label="Q5 Pops silver pouch">
  <defs>
    <linearGradient id="silverFoil" x1="0" y1="0" x2="1" y2="1">
      <stop offset="0" stop-color="var(--silver-dark)"/>
      <stop offset="0.45" stop-color="var(--white)"/>
      <stop offset="1" stop-color="var(--silver-dark)"/>
    </linearGradient>
    <radialGradient id="candyBowl" cx="0.5" cy="0.5" r="0.6">
      <stop offset="0" stop-color="var(--candy-a)"/>
      <stop offset="0.4" stop-color="var(--candy-b)"/>
      <stop offset="0.75" stop-color="var(--candy-c)"/>
      <stop offset="1" stop-color="var(--wood)"/>
    </radialGradient>
  </defs>

  <rect class="pouch-body" width="383" height="555" rx="4" fill="url(#silverFoil)"/>

  <rect class="name-band" x="0" y="309" width="365" height="80" fill="var(--black)"/>
  <rect x="0" y="307" width="365" height="3" fill="var(--red)"/>
  <rect x="0" y="389" width="365" height="3" fill="var(--red)"/>

  <ellipse role="img" aria-label="Photo of colourful jelly candies in a wooden bowl" cx="275" cy="475" rx="75" ry="72" fill="url(#candyBowl)"/>

  <path class="swoosh" d="M0,0 H383 V555 H270 C345,450 365,300 330,210 C290,110 170,70 0,88 Z" fill="var(--red)"/>
  <path class="swoosh-shade" d="M170,0 C280,40 350,130 365,260 C375,360 355,470 300,555 H330 C375,460 383,340 383,240 V0 Z" fill="var(--red-deep)" opacity="0.45"/>
  <path d="M250,0 C330,50 383,120 383,180 V0 Z" fill="var(--red-deep)" opacity="0.35"/>

  <circle class="brand-dot" cx="44" cy="160" r="17" fill="var(--red)"/>
  <text class="brand-name" x="70" y="180" font-size="54" fill="var(--red)">Q5 Pops</text>

  <text class="tagline" x="170" y="338" font-size="17" fill="var(--white)" text-anchor="middle">CBD candy infused with</text>
  <text class="product-name" x="165" y="380" font-size="44" fill="var(--white)" text-anchor="middle">DELTA-8</text>

  <g class="claims" fill="none" stroke="var(--red)" stroke-width="2">
    <circle cx="45" cy="427" r="15"/>
    <circle cx="85" cy="427" r="15"/>
    <circle cx="128" cy="427" r="16"/>
    <circle cx="177" cy="427" r="15"/>
  </g>
  <g class="icon-caption" font-size="8" fill="var(--red)" text-anchor="middle">
    <text x="45" y="455">Gluten Free</text>
    <text x="85" y="457">Vegan</text>
    <text x="128" y="459">High Protein</text>
    <text x="178" y="460">Eco Friendly</text>
  </g>

  <text class="dose" x="26" y="484" font-size="14" fill="var(--grey-text)">30mg CBD</text>
  <text class="dose" x="26" y="506" font-size="14" fill="var(--grey-text)">NET WT. 40g</text>
</svg>

<!-- Green pouch -->
<svg class="pouch pouch--green" viewBox="0 0 383 555" aria-label="Q5 Pops green pouch">
  <defs>
    <linearGradient id="labelWhite" x1="0" y1="0" x2="0" y2="1">
      <stop offset="0" stop-color="var(--white)"/>
      <stop offset="1" stop-color="var(--silver)"/>
    </linearGradient>
    <radialGradient id="gummyPile" cx="0.5" cy="0.55" r="0.6">
      <stop offset="0" stop-color="var(--candy-a)"/>
      <stop offset="0.5" stop-color="var(--candy-b)"/>
      <stop offset="1" stop-color="var(--red)" stop-opacity="0.6"/>
    </radialGradient>
  </defs>

  <rect class="pouch-top" width="383" height="310" rx="4" fill="var(--green)"/>
  <g class="pouch-stripes" fill="var(--green-deep)" opacity="0.35">
    <rect x="20" y="0" width="28" height="310"/>
    <rect x="78" y="0" width="28" height="310"/>
    <rect x="136" y="0" width="28" height="310"/>
    <rect x="194" y="0" width="28" height="310"/>
    <rect x="252" y="0" width="28" height="310"/>
    <rect x="310" y="0" width="28" height="310"/>
  </g>
  <rect class="pouch-bottom" y="309" width="383" height="246" fill="var(--red)"/>

  <path class="label-frame" d="M62,104 H322 Q322,116 334,116 V392 Q318,396 310,408 H74 Q66,396 50,392 V116 Q62,116 62,104 Z" fill="var(--black)"/>
  <path class="label-white" d="M66,110 H318 Q320,120 330,121 V388 Q316,392 308,402 H76 Q68,392 54,388 V121 Q64,120 66,110 Z" fill="url(#labelWhite)"/>
  <path class="label-red" d="M66,110 H318 Q320,120 330,121 V262 C260,244 130,244 54,262 V121 Q64,120 66,110 Z" fill="var(--red)"/>

  <circle class="brand-dot" cx="86" cy="190" r="16" fill="var(--white)"/>
  <text class="brand-name" x="112" y="210" font-size="52" fill="var(--white)">Q5 Pops</text>

  <text class="tagline" x="192" y="281" font-size="15" fill="var(--grey-text)" text-anchor="middle">CBD candy infused with</text>
  <text class="product-name" x="192" y="320" font-size="40" fill="var(--red)" text-anchor="middle">DELTA-8</text>
  <text class="script" x="192" y="341" font-size="15" fill="var(--green)" text-anchor="middle">Premium Quality</text>

  <path role="img" aria-label="Photo of a pile of colourful gummy candies" d="M58,385 C70,360 110,355 150,358 C175,345 215,345 240,358 C280,352 315,360 326,385 C300,420 90,425 58,385 Z" fill="url(#gummyPile)"/>

  <path class="ribbon" d="M80,420 Q192,460 304,420 L316,446 Q192,490 68,446 Z" fill="var(--green)" stroke="var(--white)" stroke-width="2"/>
  <path id="ribbonPath" d="M86,443 Q192,478 298,443" fill="none"/>
  <text class="ribbon-text" font-size="14" fill="var(--white)">
    <textPath href="#ribbonPath" startOffset="50%" text-anchor="middle">★ Gummy human treats ★</textPath>
  </text>

  <g class="claims" fill="none" stroke="var(--white)" stroke-width="2">
    <circle cx="64" cy="497" r="14"/>
    <circle cx="100" cy="497" r="14"/>
    <circle cx="139" cy="497" r="15"/>
    <circle cx="183" cy="499" r="14"/>
  </g>
  <g class="icon-caption" font-size="7.5" fill="var(--white)" text-anchor="middle">
    <text x="64" y="524">Gluten Free</text>
    <text x="100" y="525">Vegan</text>
    <text x="140" y="527">High Protein</text>
    <text x="184" y="528">Eco Friendly</text>
  </g>

  <text class="dose-bold" x="330" y="504" font-size="19" fill="var(--silver)" text-anchor="end">30mg CBD</text>
  <text x="330" y="526" text-anchor="end" fill="var(--silver)">
    <tspan class="dose" font-size="12">Net Wt. </tspan><tspan class="dose-bold" font-size="17">40g</tspan>
  </text>
</svg>

</body>
</html>
```